VELMIT Business Card

VELMIT (www.velmitpools.example) is a veteran in the swimming pool maintenance and repair business..we have served our clients for 15 years and have a research chemist, an electrician, a plumber and a pool building contractor (in part) on staff...We want to provide a business card that has a dual purpose, that people want to keep around, that leaves people speechless in the sense that they understand the mission of and the experience level of the TEAM at VELMIT.

Target Market(s)

persons who enjoy swimming and make it a priority to swim

Industry/Entity Type

Building

Font styles to use
Serif
Sans Serif

Colors
85acd3
3176b5
95b6d8
3276b5
0355a3
0555a3
0255a3
0455a3
85abd2

Requirements
Must have
• name, title, address, email, text
Nice to have
• a die cut shape
Should not have
• cartoons, pictures of pools

```html
<!DOCTYPE html>
<html lang="en">
<head>
<meta charset="utf-8">
<title>VELMIT Business Card</title>
<link rel="stylesheet" href="https://fonts.googleapis.com/css2?family=Open+Sans:wght@400;700&display=swap">
<style>
  :root {
    --backdrop: #2b2c2e;
    --card-white: #f4f4f4;
    --card-white-edge: #dcdcdc;
    --brand-blue: #0555a3;
    --brand-blue-light: #3276b5;
    --ink-dark: #3a3a3a;
    --ink-mid: #555555;
    --icon-grey: #6b6b6b;
    --on-blue: #e9eef5;
  }
  * { margin: 0; padding: 0; box-sizing: border-box; }
  html, body {
    width: 1200px; height: 888px; overflow: hidden;
    background: var(--backdrop);
  }
  .stage {
    position: relative; width: 1200px; height: 888px;
    display: flex; align-items: center; justify-content: center; gap: 50px;
  }
  .card {
    width: 525px; height: 300px; position: relative;
    box-shadow: 0 14px 30px rgba(0,0,0,.45);
    font-family: "Open Sans", sans-serif;
  }
  .card--contact {
    background: radial-gradient(ellipse at 45% 40%, #ffffff 0%, var(--card-white) 55%, var(--card-white-edge) 100%);
    color: var(--ink-dark);
  }
  .contact-block { position: absolute; left: 48px; top: 58px; }
  .person-name { font-weight: 700; font-size: 17px; color: var(--ink-dark); }
  .person-title { font-size: 13px; color: var(--ink-mid); margin-bottom: 12px; }
  .address { font-size: 13.5px; line-height: 1.35; color: var(--ink-mid); margin-bottom: 4px; }
  .contact-line {
    display: flex; align-items: center; gap: 8px;
    font-size: 13.5px; line-height: 1.6; color: var(--ink-mid);
  }
  .contact-line svg { width: 14px; height: 14px; flex: none; }
  .card--brand {
    background: linear-gradient(160deg, var(--brand-blue-light) 0%, var(--brand-blue) 70%);
    color: var(--on-blue);
  }
  .brand-lockup { position: absolute; left: 150px; top: 100px; }
  .brand-name {
    display: flex; align-items: center; gap: 12px;
    font-size: 44px; font-weight: 400; line-height: 1;
  }
  .brand-mark { width: 20px; height: 20px; background: var(--on-blue); }
  .tagline {
    margin-top: 14px; font-size: 14px; font-weight: 400;
  }
</style>
</head>
<body>
<main class="stage">
  <section class="card card--contact" aria-label="Business card front with contact details">
    <div class="contact-block">
      <p class="person-name">Youre Name</p>
      <p class="person-title">Marketing Manager</p>
      <p class="address">418 Harbor Lane<br>Eastport 54321</p>
      <p class="contact-line">
        <svg viewBox="0 0 14 14" aria-hidden="true"><circle cx="7" cy="7" r="7" fill="var(--icon-grey)"/><path d="M4.6 3.8c.4-.4.8-.3 1 .1l.6 1.1c.2.4 0 .7-.3 1-.2.2-.1.5.2.9.4.5.8.9 1.2 1.1.3.2.6.1.8-.2.3-.3.6-.4 1-.2l1 .6c.4.2.4.6.1 1-.7.8-1.6.9-2.6.3C6.3 8.8 5.2 7.7 4.5 6.4c-.5-1-.5-1.9.1-2.6z" fill="#fff"/></svg>
        +(000) 1234 5678
      </p>
      <p class="contact-line">
        <svg viewBox="0 0 14 14" aria-hidden="true"><circle cx="7" cy="7" r="7" fill="var(--icon-grey)"/><rect x="3.5" y="4.5" width="7" height="5" fill="none" stroke="#fff" stroke-width="1"/><path d="M3.5 4.8 7 7.4l3.5-2.6" fill="none" stroke="#fff" stroke-width="1"/></svg>
        admin@velmitpools.example
      </p>
      <p class="contact-line">
        <svg viewBox="0 0 14 14" aria-hidden="true"><circle cx="7" cy="7" r="7" fill="var(--icon-grey)"/><circle cx="7" cy="7" r="3.8" fill="none" stroke="#fff" stroke-width=".9"/><ellipse cx="7" cy="7" rx="1.6" ry="3.8" fill="none" stroke="#fff" stroke-width=".9"/><path d="M3.2 7h7.6" stroke="#fff" stroke-width=".9"/></svg>
        www.velmitpools.example
      </p>
    </div>
  </section>

  <section class="card card--brand" aria-label="Business card back with brand name">
    <div class="brand-lockup">
      <p class="brand-name"><span class="brand-mark" aria-hidden="true"></span>VELMIT</p>
      <p class="tagline">Pool care backed by one full team</p>
    </div>
  </section>
</main>
</body>
</html>
```